Natural Cosmetics need a Packaging Design

We need a PACKAGING design for labels on hand/body wash bottles and soap paper boxes.
We target at high end markets.
We expect a contemporary and trendy design.
We don't need a separate logo. The brand name "Va Mirel" acts as the logo.
We want a modern and classic font for "Va Mirel".
Please see attached pictures for packaging samples.

Industry/Entity Type

Cosmetics

Requirements
Should not have
• a separate logo from the brand name

```html
<!DOCTYPE html>
<html lang="en">
<head>
<meta charset="utf-8">
<title>Va Mirel – Hands &amp; Body Wash Label</title>
<link rel="stylesheet" href="https://fonts.googleapis.com/css2?family=Josefin+Sans:wght@200;300;400;600&display=swap">
<style>
  :root {
    --page: #ffffff;
    --label-white: #ffffff;
    --violet-deep: #3b1fb8;
    --violet: #6a4fd8;
    --lavender: #b9b3ee;
    --sky: #bfe0f7;
    --ink: #2b2640;
    --banner-top: #8a5fd6;
    --banner-bottom: #4a1c9c;
    --text-light: #ffffff;
  }
  html, body {
    margin: 0;
    padding: 0;
    width: 1200px;
    height: 1200px;
    overflow: hidden;
    background: var(--page);
  }
  .canvas {
    position: relative;
    width: 1200px;
    height: 1200px;
    background: var(--page);
    font-family: "Josefin Sans", sans-serif;
  }
  .label {
    position: absolute;
    left: 234px;
    top: 200px;
    width: 731px;
    height: 948px;
    border-radius: 18px;
    overflow: hidden;
    background: var(--label-white);
    box-shadow: 0 0 0 1px rgba(120, 120, 160, 0.08);
  }
  .label__artwork {
    position: absolute;
    inset: 0;
    width: 100%;
    height: 100%;
  }
  .brand-banner {
    position: absolute;
    left: 312px;
    top: 128px;
    width: 584px;
    height: 140px;
    border-radius: 34px;
    background: linear-gradient(180deg, var(--banner-top) 0%, var(--banner-bottom) 100%);
    display: flex;
    align-items: center;
    justify-content: center;
  }
  .brand-name {
    color: var(--text-light);
    font-family: "Josefin Sans", sans-serif;
    font-weight: 600;
    font-size: 84px;
    line-height: 1;
    letter-spacing: 1px;
    padding-top: 10px;
  }
  .product-copy {
    position: absolute;
    left: 234px;
    top: 200px;
    width: 731px;
    text-align: center;
  }
  .product-variant {
    margin: 0;
    position: absolute;
    top: 134px;
    width: 100%;
    font-weight: 400;
    font-size: 46px;
    color: var(--ink);
  }
  .product-name {
    margin: 0;
    position: absolute;
    top: 210px;
    width: 100%;
    font-weight: 200;
    font-size: 128px;
    line-height: 115px;
    color: var(--text-light);
    letter-spacing: -2px;
  }
  .product-name span { display: block; }
  .product-benefit {
    margin: 0;
    position: absolute;
    top: 566px;
    width: 100%;
    font-weight: 400;
    font-size: 40px;
    color: var(--violet-deep);
  }
</style>
</head>
<body>
<main class="canvas">
  <section class="label">
    <svg class="label__artwork" viewBox="0 0 731 948" role="img" aria-label="Abstract flowing wave artwork in violet and sky blue across the label">
      <defs>
        <linearGradient id="waveDiagonal" x1="0" y1="1" x2="1" y2="0">
          <stop offset="0" stop-color="#3b1fb8"/>
          <stop offset="0.25" stop-color="#6a7fe0"/>
          <stop offset="0.45" stop-color="#bfe0f7"/>
          <stop offset="0.62" stop-color="#b9b3ee"/>
          <stop offset="0.85" stop-color="#6a4fd8"/>
          <stop offset="1" stop-color="#3b1fb8"/>
        </linearGradient>
        <radialGradient id="whiteGlow" cx="0.85" cy="0.8" r="0.6">
          <stop offset="0" stop-color="#ffffff" stop-opacity="1"/>
          <stop offset="0.6" stop-color="#ffffff" stop-opacity="0.85"/>
          <stop offset="1" stop-color="#ffffff" stop-opacity="0"/>
        </radialGradient>
        <radialGradient id="lilacLeft" cx="0.05" cy="0.35" r="0.45">
          <stop offset="0" stop-color="#d9d4f6" stop-opacity="0.9"/>
          <stop offset="1" stop-color="#d9d4f6" stop-opacity="0"/>
        </radialGradient>
      </defs>
      <rect width="731" height="948" fill="url(#waveDiagonal)"/>
      <rect width="731" height="948" fill="url(#whiteGlow)"/>
      <rect width="731" height="948" fill="url(#lilacLeft)"/>
    </svg>
  </section>

  <div class="brand-banner">
    <span class="brand-name">Va Mirel</span>
  </div>

  <div class="product-copy">
    <p class="product-variant">moisture</p>
    <h1 class="product-name"><span>HANDS&amp;</span><span>BODY</span><span>WASH</span></h1>
    <p class="product-benefit">with vitamin e</p>
  </div>
</main>
</body>
</html>
```